Website for a company offering full serivce charging solutions for electric cars

The company "mero-kant" (english: "mero-edge") offering all-in-one-solutions for charging infrastructure for electric mobility.

There are four products:
1- Wallboxes for single-family homes
2- Solutions for property devloper/-management for property parking space
3- All-in-one-charging solution for municipalities/communities
4- Solutions for tourism/hotels/holiday appartments

The Website structure:
1. Main Page
2.1. Product Page Single Homes
2.2. Product Page Property Management / Parking
2.3. Product Page Municipality
2.4. Product Page Tourism
3. Contact Form / Request for information
4. Imprint / Legal

The Website should be built on Wordpress with a powerful possibility to simply add/modify specific landing pages.

We would like you to implement the website later and also maintain it if possible, but we would be able to do minor modifications by ourselfs (for A/B-Testing)

The website should be clear and simple, easy to understand.
Target group is mainly B2C without deeper knowledge of that topic.

It should suggest, that we will provide a very simple way to get the charging infrastructure done.

We need a contact form, maybe we will use Hubspot later.

Attached you will find a draft of the main page and a landing page (for 2.2) - it is just the content, please ignore the design. We would love to let you create a suitable design.
Also you will find some drafts a bit different for the same story.

I added also a few stock photos, but they don't need to be used! If you have better ideas, you are welcome!

Industry/Entity Type

Charging/Electric mobility

Number of Pages Required

2 page

Font styles to use
Sans Serif

Requirements
Must have
• Based on Wordpress, and the designer should be able to implement it on Wordpress on a later step

```html
<!DOCTYPE html>
<html lang="de">
<head>
<meta charset="utf-8">
<title>mero-kant.de – Designvarianten</title>
<link rel="stylesheet" href="https://fonts.googleapis.com/css2?family=Ubuntu:wght@300;400;500;700&display=swap">
<style>
:root{
  --pink:#e5128a;
  --purple:#7c5fd3;
  --lavender:#b9a6ef;
  --ink:#141218;
  --text-grey:#5a5a5f;
  --night:#0a0818;
  --board:#8f8f8f;
  --white:#ffffff;
}
*{margin:0;padding:0;box-sizing:border-box}
html,body{width:1163px;height:1200px;overflow:hidden;background:var(--board)}
body{font-family:"Ubuntu",sans-serif}
.board{position:absolute;left:0;top:0;width:1899px;height:1960px;transform:scale(.6124);transform-origin:0 0}

.page{position:absolute;overflow:hidden}
.page-light{left:45px;top:35px;width:887px;height:1897px;background:var(--white);color:var(--ink)}
.page-dark{left:976px;top:30px;width:886px;height:1836px;background:#000;color:var(--white)}

.abs{position:absolute}
.brand{position:absolute;display:flex;align-items:center;gap:8px;font-weight:400;white-space:nowrap}
.brand-dot{width:20px;height:20px;border:3px solid var(--pink);border-radius:50%}
.nav a{position:absolute;font-size:13px;font-weight:500;color:inherit;text-decoration:none;white-space:nowrap}
.search{position:absolute;width:14px;height:14px}

.btn{position:absolute;display:flex;align-items:center;justify-content:center;background:var(--pink);color:var(--white);font-weight:500;font-size:15px;border-radius:5px;height:38px}

.hero-title{position:absolute;font-size:42px;line-height:42px;font-weight:400;color:var(--white)}
.hero-sub{position:absolute;font-size:12px;line-height:16.5px;color:var(--white);font-weight:300}

.section-title{position:absolute;font-size:26px;font-weight:700}
.body-copy{position:absolute;font-size:13px;text-align:justify}
.body-copy p+p{margin-top:16px}

/* light page */
.page-light .brand{left:83px;top:18px;font-size:20px;color:#333}
.page-light .nav a{top:26px;color:#111}
.hero-photo{position:absolute;left:0;top:65px;width:887px;height:393px;border-radius:0 0 0 100px;
  background:radial-gradient(circle at 30% 25%,#c7a9f3 0,#9b74dc 30%,transparent 60%),linear-gradient(110deg,#8d6ad8 0%,#6a5bbf 45%,#3f3f55 62%,#1e2a6e 100%);
  box-shadow:0 15px 0 var(--purple)}
.about-frame{position:absolute;left:80px;top:545px;width:337px;height:317px;border-radius:14px;background:linear-gradient(135deg,#f3c6df,#c5b4f2);transform:rotate(-1.5deg)}
.about-photo{position:absolute;left:92px;top:557px;width:318px;height:298px;border-radius:10px;background:radial-gradient(circle at 55% 45%,#3f6bff 0,#2a44b8 22%,#cfd3dc 45%,#b8bcc6 100%)}
.page-light .section-title.about{left:452px;top:545px;border-top:1px solid #111;padding-top:0;line-height:30px}
.page-light .body-copy{left:454px;top:586px;width:351px;line-height:16.5px;color:var(--text-grey)}

.services-band{position:absolute;left:0;top:945px;width:887px;height:845px;border-radius:0 100px 0 100px;
  background:linear-gradient(90deg,#0b0d14,#161826 55%,#0c0d14);
  box-shadow:0 -9px 0 var(--purple),0 9px 0 var(--pink)}
.services-head{position:absolute;left:0;width:870px;text-align:center;color:var(--white)}
.services-head h2{font-size:27px;font-weight:400;display:inline-block;border-top:1px solid var(--white);line-height:32px}
.services-head p{font-size:13px;margin-top:12px}

/* service cards */
.service-card{position:absolute;width:218px;height:596px;background:var(--white);color:var(--ink)}
.card-visual{position:absolute;left:0;top:0;width:218px;height:112px;background:linear-gradient(180deg,#b05bd5 0%,#8e66d6 60%,#e8e2f6 83%,#ffffff 100%)}
.card-title{position:absolute;left:9px;top:124px;font-size:15px;font-weight:500;text-transform:uppercase;white-space:nowrap}
.card-list{position:absolute;left:8px;top:156px;width:210px;list-style:none;font-size:12.5px;line-height:19px;color:var(--text-grey)}
.card-list.dark-text{color:#222}
.card-list li{padding-left:11px;text-indent:-11px}
.card-list li.sub{padding-left:22px;text-indent:-11px}
.card-more{position:absolute;left:99px;top:542px;width:20px;height:20px}
.service-card .btn{left:54px;top:532px;width:110px}

.footer{position:absolute;font-size:13px;white-space:nowrap}
.footer span{position:absolute;top:0}
.footer .owner{font-weight:500}
.social{position:absolute;top:1px;width:15px;height:15px;border:1.2px solid currentColor;border-radius:50%}

/* dark page */
.dark-hero{position:absolute;left:0;top:0;width:886px;height:440px;background:radial-gradient(ellipse at 65% 55%,#2a1a5e 0,#180f3c 45%,#0b0720 80%),#0b0720}
.dark-hero::after{content:"";position:absolute;left:0;right:0;bottom:0;height:80px;background:linear-gradient(180deg,transparent,#000)}
.car-visual{position:absolute;left:354px;top:115px;width:500px;height:285px;border-radius:40px;background:radial-gradient(ellipse at 50% 60%,rgba(120,80,230,.35),rgba(40,20,90,.15) 55%,transparent 75%)}
.page-dark .brand{left:84px;top:18px;flex-direction:column;gap:6px;font-size:14px}
.page-dark .brand .brand-dot{width:18px;height:18px;border-width:2.5px}
.page-dark .nav a{top:30px;font-weight:700}
.page-dark .nav a.active{color:var(--pink);font-weight:400}
.collage-back{position:absolute;left:82px;top:464px;width:215px;height:276px;background:linear-gradient(160deg,#9ec9ff,#3a6ee8 40%,#c4d0e6 70%,#5f7cc0)}
.collage-outline{position:absolute;left:142px;top:498px;width:205px;height:289px;border:2px solid #7d6bd6}
.collage-front{position:absolute;left:186px;top:544px;width:218px;height:278px;border:2px solid var(--pink);background:radial-gradient(circle at 40% 25%,#dcd8ff 0,#7c76b8 25%,#3a3a48 55%,#22232c 100%)}
.collage-dot{position:absolute;left:190px;top:544px;width:18px;height:18px;border-radius:50%;background:#c62be0}
.page-dark .section-title.about{left:456px;top:462px}
.page-dark .body-copy{left:456px;top:509px;width:348px;line-height:19px;color:#e6e4ee}
.dark-services{position:absolute;left:0;top:898px;width:886px;height:807px;background:#0d0b13}
.dark-services h2{position:absolute;left:0;top:54px;width:886px;text-align:center;font-size:27px;font-weight:400}
</style>
</head>
<body>
<div class="board">

  <!-- Light variant -->
  <section class="page page-light">
    <header>
      <div class="brand"><span class="brand-dot"></span>mero-kant.de</div>
      <nav class="nav">
        <a style="left:325px">Lösungen</a>
        <a style="left:420px">Unternehmen</a>
        <a style="left:540px">Services</a>
        <a style="left:627px">Karriere</a>
        <a style="left:713px">Kontakt</a>
      </nav>
      <svg class="search" style="left:787px;top:25px" viewBox="0 0 14 14"><circle cx="6" cy="6" r="4.5" fill="none" stroke="#111" stroke-width="1.6"/><line x1="9.3" y1="9.3" x2="13" y2="13" stroke="#111" stroke-width="1.6"/></svg>
    </header>

    <div class="hero-photo" role="img" aria-label="Ladestecker steckt in einer Ladesäule, violettes Bokeh im Hintergrund"></div>
    <h1 class="hero-title" style="left:80px;top:155px">Willkommen zu<br>Mero-kant.de</h1>
    <p class="hero-sub" style="left:83px;top:245px">wenn das Laden nicht nur einfach, sondern<br>die Umsetzung auch aus einer Hand<br>kommen soll.</p>
    <a class="btn" style="left:83px;top:303px;width:97px">Loslegen</a>

    <div class="about-frame"></div>
    <div class="about-photo" role="img" aria-label="Ladekabel an einem Elektroauto mit blau leuchtendem Ladeanschluss"></div>
    <h2 class="section-title about">Über Mero-kant.de</h2>
    <div class="body-copy">
      <p>wenn das Laden nicht nur einfach, sondern die Umsetzung auch aus einer Hand kommen soll.Wir bieten Lösungen sowohl für Privatkunden, Geschäftskunden als auch Kommunen an, die schnell, fair und ohne Eigenleistung zu einer smarten Ladelösung für E-Fahrzeuge kommen möchten.</p>
      <p>Von der Beratung, über die Installation, Inbetriebnahme bis zur Abrechnung und Wartung bekommen Sie bei mero-kant alles aus einer Hand. Auf Wunsch vermieten wir auch die Ladetechnik und übernehmen im gewerblichen Bereich die direkte Abrechnung mit dem Nutzer. Für Kommunen bieten wir den kostenfreien Full-Service an und beteiligen die Gemeinden an der Nutzung der Infrastruktur.</p>
    </div>
    <a class="btn" style="left:452px;top:815px;width:109px">Weiterlesen</a>

    <div class="services-band"></div>
    <div class="services-head" style="top:1018px">
      <h2>Unsere Dienstleistungen</h2>
      <p>Fragen Sie uns nach der auf Ihre individuellen Bedürfnisse zugeschnittenen Lösung</p>
    </div>

    <article class="service-card" style="left:83px;top:1104px">
      <div class="card-visual" role="img" aria-label="Weißes Elektroauto an einer Ladesäule vor violettem Hintergrund"></div>
      <h3 class="card-title">Als Privatkunde</h3>
      <ul class="card-list">
        <li>→ Bestandsanalyse mit umfangreicher Beratung über die Möglichkeiten der Umsetzung.</li>
        <li>→ Prüfung und Übernahme der Anmeldung verfügbarer Fördermöglichkeiten.</li>
        <li>→ Auswahl an smarten Wallbox Lösungen, passend für Ihr Fahrzeug und Ihre BedürfnisseInstallation inkl.</li>
        <li>→ Aller notwendigen Materialien und Tätigkeiten (Durchbrüche, Erdarbeiten, etc.).</li>
        <li>→ Inbetrie - bnahme und Einweisung in die.</li>
        <li>→ Ladetechnik Jährlich technische Wartung nach DGUV3 Reparatur service, unter Berücksichtigung der geltenden Garantie Ansprüche.</li>
      </ul>
      <svg class="card-more" viewBox="0 0 20 20"><circle cx="10" cy="10" r="10" fill="#6b4fd0"/><path d="M5 10h9M10.5 6l4 4-4 4" fill="none" stroke="#fff" stroke-width="2"/></svg>
    </article>

    <article class="service-card" style="left:335px;top:1104px">
      <div class="card-visual" role="img" aria-label="Weißes Elektroauto an einer Ladesäule vor violettem Hintergrund"></div>
      <h3 class="card-title">Als Geschäftskunde</h3>
      <ul class="card-list dark-text">
        <li>→ Durchführung einer individuellen Bedarfsanalyse inkl. Ermittlung der Anforderungen für:</li>
        <li class="sub">- Haus- und Immobilienver waltungen</li>
        <li class="sub">- Dienstleistungs- und Handelsunternehmen</li>
        <li class="sub">- Hotel und Beherbergungsbetriebe</li>
        <li class="sub">- Parkraum- und Parkhausbetreiber</li>
        <li class="sub">- Tourismus, Sport- und Freizeitei richtungen.</li>
        <li>→ Planung und Projektierung des Installation saufwands inkl. Materialver brauch.</li>
        <li>→ Leasing oder Kauf der Hardware.</li>
        <li>→ Normgerechte Installation der Ladeinfrastruktur inkl.</li>
      </ul>
      <a class="btn">Weiterlesen</a>
    </article>

    <article class="service-card" style="left:586px;top:1104px">
      <div class="card-visual" role="img" aria-label="Weißes Elektroauto an einer Ladesäule vor violettem Hintergrund"></div>
      <h3 class="card-title">Als Kommune</h3>
      <ul class="card-list">
        <li>→ Konzeptionierung möglicher. Ladeinfrastrukturen innerhalb Ihrer Gemeinde.</li>
        <li>→ Planung und Projektsteuerung inkl.</li>
        <li>→ sämtlicher behördlicher Genehmigungsverfahren und Beantragung von Fördermitteln.</li>
        <li>→ Fachgerechte Installation und Inbetriebnahme. Regelmäßige Wartung gemäß Vorschrif.</li>
        <li>→ Reparatur und Kundenservice. Direkte Abrechnung mit dem Nutzer.</li>
        <li>→ Beteiligung der Gemeinde am Umsatz.</li>
        <li>→ Möglichkeit der Integration von Bonus programmen, mit denen der lokale Einzelhandel beworben wird.</li>
      </ul>
      <svg class="card-more" viewBox="0 0 20 20"><circle cx="10" cy="10" r="10" fill="#6b4fd0"/><path d="M5 10h9M10.5 6l4 4-4 4" fill="none" stroke="#fff" stroke-width="2"/></svg>
    </article>

    <footer class="footer" style="left:0;top:1838px;width:887px;color:#222">
      <span class="owner" style="left:83px">©mero-kant GmbH</span>
      <span style="left:232px">AGB</span>
      <span style="left:281px">Datenschutzerklarung</span>
      <span style="left:431px">Impressum</span>
      <span style="left:517px">Kontakt</span>
      <span style="left:586px">Karriere</span>
      <span style="left:657px">FAQs</span>
      <i class="social" style="left:723px"></i>
      <i class="social" style="left:756px"></i>
      <i class="social" style="left:789px"></i>
    </footer>
  </section>

  <!-- Dark variant -->
  <section class="page page-dark">
    <div class="dark-hero"></div>
    <div class="car-visual" role="img" aria-label="Silhouette eines Sportwagens neben einer Ladesäule in violettem Licht"></div>
    <header>
      <div class="brand"><span class="brand-dot"></span>mero-kant.de</div>
      <nav class="nav">
        <a class="active" style="left:263px">Lösungen</a>
        <a style="left:370px">Unternehmen</a>
        <a style="left:502px">Services</a>
        <a style="left:600px">Karriere</a>
        <a style="left:699px">Kontakt</a>
      </nav>
      <svg class="search" style="left:787px;top:30px" viewBox="0 0 14 14"><circle cx="6" cy="6" r="4.5" fill="none" stroke="#fff" stroke-width="1.6"/><line x1="9.3" y1="9.3" x2="13" y2="13" stroke="#fff" stroke-width="1.6"/></svg>
    </header>

    <h1 class="hero-title" style="left:82px;top:152px">Willkommen zu<br>Mero-kant.de</h1>
    <p class="hero-sub" style="left:84px;top:240px">wenn das Laden nicht nur einfach, sondern<br>die Umsetzung auch aus einer Hand<br>kommen soll.</p>
    <a class="btn" style="left:84px;top:300px;width:97px">Loslegen</a>

    <div class="collage-back" role="img" aria-label="Ladestecker mit blau leuchtendem Ring am Fahrzeug"></div>
    <div class="collage-outline"></div>
    <div class="collage-front" role="img" aria-label="Ladestecker in einer Ladesäule mit Lichtern im Hintergrund"></div>
    <div class="collage-dot"></div>
    <h2 class="section-title about">Über Mero-kant.de</h2>
    <div class="body-copy">
      <p>wenn das Laden nicht nur einfach, sondern die Umsetzung auch aus einer Hand kommen soll.Wir bieten Lösungen sowohl für Privatkunden, Geschäftskunden als auch Kommunen an, die schnell, fair und ohne Eigenleistung zu einer smarten Ladelösung für E-Fahrzeuge kommen möchten.</p>
      <p>Von der Beratung, über die Installation, Inbetriebnahme bis zur Abrechnung und Wartung bekommen Sie bei mero-kant alles aus einer Hand. Auf Wunsch vermieten wir auch die Ladetechnik und übernehmen im gewerblichen Bereich die direkte Abrechnung mit dem Nutzer. Für Kommunen bieten wir den kostenfreien Full-Service an und beteiligen die Gemeinden an der Nutzung der Infrastruktur.</p>
    </div>
    <a class="btn" style="left:457px;top:793px;width:110px">Weiterlesen</a>

    <div class="dark-services"><h2>Unsere Dienstleistungen</h2></div>

    <article class="service-card" style="left:81px;top:1021px">
      <div class="card-visual" role="img" aria-label="Weißes Elektroauto an einer Ladesäule vor violettem Hintergrund"></div>
      <h3 class="card-title">Als Privatkunde</h3>
      <ul class="card-list">
        <li>→ Bestandsanalyse mit umfangreicher Beratung über die Möglichkeiten der Umsetzung.</li>
        <li>→ Prüfung und Übernahme der Anmeldung verfügbarer Fördermöglichkeiten.</li>
        <li>→ Auswahl an smarten Wallbox Lösungen, passend für Ihr Fahrzeug und Ihre BedürfnisseInstallation inkl.</li>
        <li>→ Aller notwendigen Materialien und Tätigkeiten (Durchbrüche, Erdarbeiten, etc.).</li>
        <li>→ Inbetrie - bnahme und Einweisung in die.</li>
        <li>→ Ladetechnik Jährlich technische Wartung nach DGUV3 Reparatur service, unter Berücksichtigung der geltenden Garantie Ansprüche.</li>
      </ul>
      <svg class="card-more" viewBox="0 0 20 20"><circle cx="10" cy="10" r="10" fill="#6b4fd0"/><path d="M5 10h9M10.5 6l4 4-4 4" fill="none" stroke="#fff" stroke-width="2"/></svg>
    </article>

    <article class="service-card" style="left:333px;top:1021px">
      <div class="card-visual" role="img" aria-label="Weißes Elektroauto an einer Ladesäule vor violettem Hintergrund"></div>
      <h3 class="card-title">Als Geschäftskunde</h3>
      <ul class="card-list dark-text">
        <li>→ Durchführung einer individuellen Bedarfsanalyse inkl. Ermittlung der Anforderungen für:</li>
        <li class="sub">- Haus- und Immobilienver waltungen</li>
        <li class="sub">- Dienstleistungs- und Handelsunternehmen</li>
        <li class="sub">- Hotel und Beherbergungsbetriebe</li>
        <li class="sub">- Parkraum- und Parkhausbetreiber</li>
        <li class="sub">- Tourismus, Sport- und Freizeitei richtungen.</li>
        <li>→ Planung und Projektierung des Installation saufwands inkl. Materialver brauch.</li>
        <li>→ Leasing oder Kauf der Hardware.</li>
        <li>→ Normgerechte Installation der Ladeinfrastruktur inkl.</li>
      </ul>
      <a class="btn">Weiterlesen</a>
    </article>

    <article class="service-card" style="left:584px;top:1021px">
      <div class="card-visual" role="img" aria-label="Weißes Elektroauto an einer Ladesäule vor violettem Hintergrund"></div>
      <h3 class="card-title">Als Kommune</h3>
      <ul class="card-list">
        <li>→ Konzeptionierung möglicher. Ladeinfrastrukturen innerhalb Ihrer Gemeinde.</li>
        <li>→ Planung und Projektsteuerung inkl.</li>
        <li>→ sämtlicher behördlicher Genehmigungsverfahren und Beantragung von Fördermitteln.</li>
        <li>→ Fachgerechte Installation und Inbetriebnahme. Regelmäßige Wartung gemäß Vorschrif.</li>
        <li>→ Reparatur und Kundenservice. Direkte Abrechnung mit dem Nutzer.</li>
        <li>→ Beteiligung der Gemeinde am Umsatz.</li>
        <li>→ Möglichkeit der Integration von Bonus programmen, mit denen der lokale Einzelhandel beworben wird.</li>
      </ul>
      <svg class="card-more" viewBox="0 0 20 20"><circle cx="10" cy="10" r="10" fill="#6b4fd0"/><path d="M5 10h9M10.5 6l4 4-4 4" fill="none" stroke="#fff" stroke-width="2"/></svg>
    </article>

    <footer class="footer" style="left:0;top:1760px;width:886px;color:#fff">
      <span class="owner" style="left:82px">©mero-kant GmbH</span>
      <span style="left:230px">AGB</span>
      <span style="left:279px">Datenschutzerklarung</span>
      <span style="left:429px">Impressum</span>
      <span style="left:516px">Kontakt</span>
      <span style="left:585px">Karriere</span>
      <span style="left:655px">FAQs</span>
      <i class="social" style="left:722px"></i>
      <i class="social" style="left:754px"></i>
      <i class="social" style="left:787px"></i>
    </footer>
  </section>

</div>
</body>
</html>
```